Design a Website Mockup for a Start-Up Competition

The website is meant for start-ups to register their idea for a start-up competition in Singapore. The new start-ups, founders, entrepreneurs will register their interest to participate in the competition. After a formal screening and selection process, the winners will get equity investments as prize money. The target audience/visitors for our website are IT, Technology, Internet, Internet of Things related start-ups. The graphics and images that you create as part of the mock up need to reflect "Internet of Things".

We are looking for a clean and fresh design for the web site.

The MAIN LANDING PAGE navigation menu bar on the top will look something like this:
Home --> About; Contact Us
Challenge --> Overview; Competition Details; Rules; Judges; FAQ
Prize --> Equity Investments for Singaporean Start-ups ; Overseas Immersion Program in USA
Mentors --> Mentor Benefits; Mentor Commitments; Become a Mentor
Partners --> Partner Benefits; Become a Partner; Empower a start-up
Sponsors
Blog

The MAIN LANDING PAGE design could be something inspired based on "http://www.brovalumhub.com/startup-competition/how-it-works/". Please do NOT copy. Use this for inspiration only. Get creative, be original and make it impressive.

Common for all pages at the bottom:
Tavorine Quellap Lumvarett Dovrane icons

Sign Up For Our Newsletter

Contact Us; Privacy & Cookies; Terms of Use; KOVA 9 © 2015 Singapore

Common for all pages at the top right:
"Register / Login" button. When the user clicks the "Register / Login" button, then it should open a new window, which will look like the enclosed "Login page.pdf". There will be 4 blocks (categories) of users. We want to have the Singapore skyline in the background and a very simple login page, as shown in the enclosed picture. Use this for inspiration only. Be creative and come out with cool ideas to impress! Once the user clicks on one of the 4 blocks, it
will open a pop-up window for login. The login page will be a small pop-up window with conventional login page with USER NAME, PASSWORD, New users to REGISTER, Forgot UserName, Password etc. The enclosed image is to be used for the Singapore skyline. (Copyrighted image).

Company logo has been uploaded now. Please remove the BRAVUL (text part from the logo) and use only the image part.

```html
<!DOCTYPE html>
<html lang="en">
<head>
<meta charset="utf-8">
<title>KOVA 9 — Startup Challenge</title>
<link rel="stylesheet" href="https://fonts.googleapis.com/css2?family=Arimo:wght@400;700&family=Open+Sans:wght@400;600&display=swap">
<style>
  :root{
    --white:#ffffff;
    --ink:#1a1a1a;
    --muted:#555b60;
    --nav:#1c3556;
    --footer:#11212b;
    --panel:rgba(20,24,34,.72);
    --divider:rgba(120,150,190,.45);
    --green:#3db34a;
    --blue:#4cb2f2;
    --pink:#f26ee9;
    --orange:#f7a846;
    --sub-yellow:#f2e04b;
    --sub-blue:#5bb8f5;
    --sub-pink:#f27df0;
    --sub-orange:#f5b54f;
    --field:#dcdcdc;
    --footer-text:#c9d2d8;
  }
  *{margin:0;padding:0;box-sizing:border-box}
  html,body{width:1200px;height:1168px;overflow:hidden}
  body{position:relative;background:var(--white);font-family:"Arimo",Arial,sans-serif;color:var(--ink)}

  .site-header{position:absolute;left:0;top:0;width:1200px;height:68px;background:var(--white)}
  .brand{position:absolute;left:227px;top:16px;display:flex;align-items:center;gap:8px;font:700 26px/1 "Arimo",sans-serif;color:var(--ink);letter-spacing:1px}
  .brand-dot{width:14px;height:14px;border-radius:50%;background:var(--ink)}
  .helpline{position:absolute;left:649px;top:30px;font-size:11px;color:var(--muted);letter-spacing:.3px}
  .account{position:absolute;left:859px;top:29px;font-size:11px;color:var(--muted);display:flex;align-items:center;gap:5px;letter-spacing:.3px}

  .main-nav{position:absolute;left:0;top:68px;width:1200px;height:38px;background:linear-gradient(90deg,#1b2f4c,#22426a 60%,#1e3a5e)}
  .main-nav ul{list-style:none}
  .main-nav li{position:absolute;top:12px;font-size:13px;color:var(--white);letter-spacing:.3px}

  .hero{position:absolute;left:0;top:106px;width:1200px;height:761px;
    background:
      linear-gradient(180deg,rgba(0,0,0,0) 0%,rgba(0,0,0,0) 78%,#2a3a5a 79%,#3d5478 88%,#2d3f5e 100%),
      linear-gradient(180deg,#1f4f8c 0%,#4f86c0 22%,#6e9bc8 38%,#3b5e94 55%,#1d2f55 72%,#202e4c 78%),
      linear-gradient(90deg,rgba(0,0,0,0) 70%,rgba(240,140,150,.35) 100%);
    background-blend-mode:normal,normal,screen}
  .hero-glow{position:absolute;right:0;top:160px;width:260px;height:220px;background:radial-gradient(ellipse at 80% 50%,rgba(245,150,150,.55),rgba(0,0,0,0) 70%)}

  .audience-panel{position:absolute;left:224px;top:488px;width:751px;height:256px;background:var(--panel);display:flex}
  .audience{flex:1;text-align:center;position:relative}
  .audience + .audience{border-left:1px solid var(--divider)}
  .audience h2{margin-top:36px;font:400 24px/1 "Open Sans",sans-serif;color:var(--white);letter-spacing:.3px}
  .audience .tagline{margin-top:7px;font-size:14px;letter-spacing:.2px}
  .audience p{margin-top:14px;font-size:12.5px;line-height:18px;color:var(--white)}
  .audience .cta{position:absolute;left:50%;top:172px;transform:translateX(-50%);width:120px;height:32px;line-height:32px;font-size:12.5px;font-weight:700;color:var(--white);letter-spacing:.3px}
  .startups .tagline{color:var(--sub-yellow)} .startups .cta{background:var(--green)}
  .mentors .tagline{color:var(--sub-blue)} .mentors .cta{background:var(--blue)}
  .partners .tagline{color:var(--sub-pink)} .partners .cta{background:var(--pink)}
  .smes .tagline{color:var(--sub-orange)} .smes .cta{background:var(--orange)}

  .site-footer{position:absolute;left:0;top:867px;width:1200px;height:301px;background:var(--footer);color:var(--white)}
  .footer-brand{position:absolute;left:229px;top:80px;display:flex;align-items:center;gap:12px;font:700 44px/1 "Arimo",sans-serif;color:var(--white);letter-spacing:1px}
  .footer-brand .brand-dot{width:22px;height:22px;background:var(--white)}
  .legal{position:absolute;left:227px;top:152px;font-size:10.5px;line-height:13px;color:var(--footer-text)}
  .legal span{margin-right:6px}

  .newsletter{position:absolute;left:569px;top:56px}
  .newsletter h3,.social h3{font:400 19px/1 "Open Sans",sans-serif;color:var(--white)}
  .field{display:block;width:174px;height:30px;margin-top:8px;background:var(--field);font-size:9px;color:#666;line-height:30px;padding-left:11px}
  .newsletter h3 + .field{margin-top:11px}
  .submit{display:block;width:76px;height:28px;margin-top:11px;background:var(--orange);color:var(--ink);font-size:13px;line-height:28px;padding-left:12px}

  .social{position:absolute;left:896px;top:56px}
  .social ul{list-style:none;margin-top:14px}
  .social li{display:flex;align-items:center;gap:10px;height:20px;font-size:12.5px;color:var(--white)}
  .social .mark{width:9px;height:9px;background:var(--white)}
</style>
</head>
<body>
  <header class="site-header">
    <div class="brand"><span class="brand-dot"></span>KOVA 9</div>
    <div class="helpline">HELPLINE &nbsp;+0000 482 7150</div>
    <div class="account">
      <svg width="9" height="11" viewBox="0 0 9 11" aria-hidden="true"><rect x="0.5" y="4.5" width="8" height="6" fill="#777"/><path d="M2.5 4.5V3a2 2 0 0 1 4 0" stroke="#777" fill="none"/></svg>
      LOGIN &nbsp;/&nbsp; REGISTER
    </div>
  </header>

  <nav class="main-nav">
    <ul>
      <li style="left:225px">HOME</li>
      <li style="left:288px">CHALLENGE</li>
      <li style="left:391px">PRICE</li>
      <li style="left:457px">MENTORS</li>
      <li style="left:547px">PARTNERS</li>
    </ul>
  </nav>

  <section class="hero" role="img" aria-label="City skyline at dusk reflected in a bay, seen from a wooden pier">
    <div class="hero-glow"></div>
  </section>

  <div class="audience-panel">
    <div class="audience startups">
      <h2>STARTUPS</h2>
      <div class="tagline">ENTER THE CONTEST</div>
      <p>This is dumy content<br>please change with<br>orginal content</p>
      <div class="cta">LOGIN NOW</div>
    </div>
    <div class="audience mentors">
      <h2>MENTORS</h2>
      <div class="tagline">BECOME A MENTOR</div>
      <p>This is dumy content<br>please change with<br>orginal content</p>
      <div class="cta">LOGIN NOW</div>
    </div>
    <div class="audience partners">
      <h2>PARTNERS</h2>
      <div class="tagline">BUILD THE NETWORKS</div>
      <p>This is dumy content<br>please change with<br>orginal content</p>
      <div class="cta">LOGIN NOW</div>
    </div>
    <div class="audience smes">
      <h2>SMES</h2>
      <div class="tagline">GO INTERNATIONAL</div>
      <p>This is dumy content<br>please change with<br>orginal content</p>
      <div class="cta">LOGIN NOW</div>
    </div>
  </div>

  <footer class="site-footer">
    <div class="footer-brand"><span class="brand-dot"></span>KOVA 9</div>
    <div class="legal">
      <span>Contact Us &nbsp;I</span><span>Privacy &amp; Cookies &nbsp;&nbsp;I</span><span>Terms of Use</span><br>
      KOVA 9 © 2015 Singapore
    </div>

    <div class="newsletter">
      <h3>News letter</h3>
      <span class="field">Name</span>
      <span class="field">Email ID</span>
      <span class="submit">Submit</span>
    </div>

    <div class="social">
      <h3>Follow Us</h3>
      <ul>
        <li><span class="mark"></span>Tavorine</li>
        <li><span class="mark"></span>Quellap</li>
        <li><span class="mark"></span>Dovrane</li>
        <li><span class="mark"></span>Lumvarett</li>
      </ul>
    </div>
  </footer>
</body>
</html>
```